Starting meadery needs logo and label design

We are starting to show our hand crafted meads to potential investors and need a professional logo and label to properly show how serious this proj...

Target Market(s)

Craft beer drinker searching for a new experience. People who are beer drinkers aspiring to be wine drinker.

Industry/Entity Type

It Professional

Requirements
Must have
• Professional design. Not overly ornate. Simple use of colors for low cost startup printing.

```html
<!DOCTYPE html>
<html lang="en">
<head>
<meta charset="utf-8">
<title>MCDX Meadery – Honey Wine Labels</title>
<link rel="stylesheet" href="https://fonts.googleapis.com/css2?family=Josefin+Sans:wght@400;700&display=swap">
<style>
  :root {
    --bg: #c9cfc6;
    --paper: #ffffff;
    --ink: #0d0d0d;
    --honey: #f9c220;
  }
  html, body {
    margin: 0;
    padding: 0;
    width: 1200px;
    height: 1000px;
    overflow: hidden;
    background: var(--bg);
  }
  .canvas {
    position: relative;
    width: 1200px;
    height: 1000px;
    font-family: "Josefin Sans", "Century Gothic", sans-serif;
  }
  .label {
    position: absolute;
    top: 115px;
    width: 500px;
    height: 770px;
    overflow: hidden;
  }
  .label--light { left: 70px; }
  .label--dark  { left: 630px; }

  .label__top {
    position: absolute;
    left: 0; top: 0;
    width: 100%;
    height: 450px;
    background: var(--paper);
  }
  .label--dark .label__top { background: var(--ink); }

  .label__bottom {
    position: absolute;
    left: 0; top: 450px;
    width: 100%;
    height: 320px;
    background: var(--honey);
  }
  .label__frame {
    position: absolute;
    left: 0; top: 0;
    width: 500px;
    height: 770px;
  }
  .brand {
    position: absolute;
    left: 0; right: 0;
    top: 120px;
    text-align: center;
    color: var(--ink);
    font-weight: 700;
  }
  .label--dark .brand { color: var(--paper); }
  .brand__mark {
    display: block;
    width: 56px;
    height: 56px;
    margin: 0 auto 36px;
    background: currentColor;
  }
  .brand__name {
    display: block;
    font-size: 96px;
    line-height: 1;
    letter-spacing: 2px;
  }
  .brand__sub {
    display: block;
    margin-top: 14px;
    font-size: 40px;
    line-height: 1;
    letter-spacing: 1px;
  }
  .tagline {
    position: absolute;
    left: 0; right: 0;
    top: 472px;
    text-align: center;
    color: var(--ink);
    font-weight: 400;
    font-size: 20px;
    line-height: 23px;
    letter-spacing: 0.5px;
  }
  .volume {
    position: absolute;
    left: 0; right: 0;
    top: 668px;
    text-align: center;
    color: var(--ink);
    font-size: 32px;
    font-weight: 400;
  }
</style>
</head>
<body>
<main class="canvas">

  <section class="label label--light" aria-label="Light label">
    <div class="label__top"></div>
    <div class="label__bottom"></div>
    <svg class="label__frame" viewBox="0 0 500 770" aria-hidden="true">
      <path d="M42 22 H458 A20 20 0 0 0 478 42 V728 A20 20 0 0 0 458 748 H42 A20 20 0 0 0 22 728 V42 A20 20 0 0 0 42 22 Z"
            fill="none" stroke="#0d0d0d" stroke-width="3"/>
    </svg>
    <h1 class="brand">
      <span class="brand__mark"></span>
      <span class="brand__name">MCDX</span>
      <span class="brand__sub">MEADERY</span>
    </h1>
    <p class="tagline">HAND CRAFTED<br>Honey Wine</p>
    <p class="volume">750ml</p>
  </section>

  <section class="label label--dark" aria-label="Dark label">
    <div class="label__top"></div>
    <div class="label__bottom"></div>
    <svg class="label__frame" viewBox="0 0 500 770" aria-hidden="true">
      <defs>
        <clipPath id="frame-top"><rect x="0" y="0" width="500" height="450"/></clipPath>
        <clipPath id="frame-bottom"><rect x="0" y="450" width="500" height="320"/></clipPath>
      </defs>
      <path clip-path="url(#frame-top)" d="M42 22 H458 A20 20 0 0 0 478 42 V728 A20 20 0 0 0 458 748 H42 A20 20 0 0 0 22 728 V42 A20 20 0 0 0 42 22 Z"
            fill="none" stroke="#ffffff" stroke-width="3"/>
      <path clip-path="url(#frame-bottom)" d="M42 22 H458 A20 20 0 0 0 478 42 V728 A20 20 0 0 0 458 748 H42 A20 20 0 0 0 22 728 V42 A20 20 0 0 0 42 22 Z"
            fill="none" stroke="#0d0d0d" stroke-width="3"/>
    </svg>
    <h2 class="brand">
      <span class="brand__mark"></span>
      <span class="brand__name">MCDX</span>
      <span class="brand__sub">MEADERY</span>
    </h2>
    <p class="tagline">HAND CRAFTED<br>Honey Wine</p>
    <p class="volume">750ml</p>
  </section>

</main>
</body>
</html>
```